Professional Services - letterhead / business cards

The company (velmora holdings) will provide services to Investment Funds and large investors in Spain. I have recently chosen a logo that I am attaching.

I would like a simple stationary design that i could use as letter head, business cards and "with compliments" cards.

I am not quite sure which color I will mostly use for the logo, in the email signature I will probably lean towards the white background and grey letters. I am attaching my favourite options.

Target Market(s)

Large Multinationals, Investment funds and Law firms

Industry/Entity Type

Business

Requirements
Must have
• my details are:
Luis R. Albarda
Velmora Holdings S.L.
Casa de Valdetorres
Calle de Ortuzar Beltrán 27
28019 Madrid
T: +34 (91) 387-6051
M: +34 (655) 814-073
e-mail: lalbarda@velmoraholdings.example

```html
<!DOCTYPE html>
<html lang="en">
<head>
<meta charset="utf-8">
<title>Velmora Holdings – Stationery Set</title>
<link rel="stylesheet" href="https://fonts.googleapis.com/css2?family=Open+Sans:wght@400;600;700&display=swap">
<style>
  :root {
    --backdrop: #9b9b9d;
    --paper: #f1f1f2;
    --paper-edge: #dcdcde;
    --accent: #34306a;
    --ink: #4a4a4f;
    --ink-soft: #6d6d73;
    --window: #b9b9bc;
    --signature: #d9d9dc;
  }
  * { margin: 0; padding: 0; box-sizing: border-box; }
  html, body { width: 1200px; height: 1049px; overflow: hidden; }
  body {
    background: var(--backdrop);
    font-family: "Open Sans", Arial, sans-serif;
    color: var(--ink);
    position: relative;
  }
  .sheet {
    position: absolute;
    background: var(--paper);
    border: 1px solid var(--paper-edge);
    box-shadow: 0 6px 18px rgba(0,0,0,0.18);
  }
  .company-name {
    font-family: "Open Sans", Arial, sans-serif;
    font-weight: 400;
    color: var(--ink);
    white-space: nowrap;
    line-height: 1.2;
  }
  .contact-block {
    font-size: 8px;
    line-height: 1.5;
    color: var(--ink-soft);
  }

  /* Letterhead */
  .letterhead { left: 60px; top: 56px; width: 480px; height: 679px; padding: 52px 56px; }
  .letterhead .company-name { font-size: 20px; }
  .letter-body { margin-top: 46px; font-size: 8.5px; line-height: 1.65; color: var(--ink); }
  .letter-body .salutation { font-weight: 700; margin-bottom: 12px; }
  .letter-body p { margin-bottom: 12px; }
  .sign-off { margin-top: 30px; }
  .signature-area { width: 110px; height: 38px; background: var(--signature); border-radius: 3px; }
  .sign-off .role { font-size: 8.5px; font-weight: 700; margin-top: 6px; color: var(--ink); }
  .letterhead .contact-block { position: absolute; left: 210px; bottom: 44px; }

  /* Envelope */
  .envelope { left: 600px; top: 56px; width: 540px; height: 270px; padding: 40px 44px; }
  .envelope .company-name { font-size: 17px; }
  .envelope-window {
    position: absolute; left: 250px; top: 132px; width: 220px; height: 78px;
    background: var(--window); border: 1px solid #aaaaae; border-radius: 2px;
  }

  /* Compliments slip */
  .compliments { left: 600px; top: 380px; width: 540px; height: 270px; }
  .compliments .greeting {
    position: absolute; right: 44px; top: 40px;
    font-size: 13px; color: var(--accent);
  }
  .compliments .company-name { position: absolute; left: 44px; top: 148px; font-size: 20px; }
  .compliments .contact-block { position: absolute; left: 44px; bottom: 30px; }

  /* Business card */
  .business-card { left: 60px; top: 790px; width: 320px; height: 180px; padding: 30px 28px; }
  .business-card .company-name { font-size: 15px; }
  .business-card .card-name {
    margin-top: 22px; font-size: 8px; letter-spacing: 0.12em;
    text-transform: uppercase; color: var(--ink); font-weight: 600;
  }
  .business-card .contact-block { margin-top: 8px; font-size: 7.5px; }
</style>
</head>
<body>

  <section class="sheet letterhead" aria-label="Letterhead">
    <div class="company-name">velmora holdings</div>
    <div class="letter-body">
      <p class="salutation">Dear Sir or Madam,</p>
      <p>Thank you for your recent enquiry regarding our advisory services for investment funds and institutional investors in Spain. We are pleased to outline how our team can support your transactions from initial review to final closing.</p>
      <p>Our professionals bring local knowledge of property, tax and regulatory matters, working closely with your legal advisers to keep every step clear and well documented.</p>
      <p>We would welcome the opportunity to meet and discuss your plans in more detail at a time that suits you.</p>
      <p>Please do not hesitate to contact me directly should you have any questions.</p>
      <div class="sign-off">
        <div class="signature-area" role="img" aria-label="Handwritten signature"></div>
        <div class="role">Company Director</div>
      </div>
    </div>
    <div class="contact-block">
      Calle de Ortuzar Beltrán 27, 2ºA<br>
      Casa de Valdetorres, 28019 Madrid<br>
      T +34 (91) 387-6051 · M +34 (655) 814-073
    </div>
  </section>

  <section class="sheet envelope" aria-label="Envelope">
    <div class="company-name">velmora holdings</div>
    <div class="envelope-window"></div>
  </section>

  <section class="sheet compliments" aria-label="With compliments slip">
    <div class="greeting">With compliments</div>
    <div class="company-name">velmora holdings</div>
    <div class="contact-block">
      Calle de Ortuzar Beltrán 27, 2ºA<br>
      Casa de Valdetorres, 28019 Madrid<br>
      T +34 (91) 387-6051 · M +34 (655) 814-073<br>
      E lalbarda@velmoraholdings.example
    </div>
  </section>

  <section class="sheet business-card" aria-label="Business card">
    <div class="company-name">velmora holdings</div>
    <div class="card-name">Luis R. Albarda</div>
    <div class="contact-block">
      Calle de Ortuzar Beltrán 27, 2ºA<br>
      Casa de Valdetorres, 28019 Madrid<br>
      T +34 (91) 387-6051 · M +34 (655) 814-073<br>
      E lalbarda@velmoraholdings.example
    </div>
  </section>

</body>
</html>
```